Welcome signage for KJT Software Consulting Company

I need Welcome signage for KJT Consulting company Office Window. We are a Computer software company that offers software Implementation and Training for our Customers windows size 1. 900mm high 750mm wide. size 2. 1000mm high 700 wide.
Please review our website for branding and ideas.
The poster needs to contain our logo, website www.kjtconsulting-example.net.au and ph number 1300 46 81 07 , and the strap line... Empowering businesses with software choice.
Updates

Hi I'm really keen to find the perfect design. I had decided on one however the designer was dismissed from the group by admin so here I go again. Please read the briefs already in the information and hopefully I am excited by new submissions when I arrive to work on Monday xxx Thanks heaps fellow Designers x

```html
<!DOCTYPE html>
<html lang="en">
<head>
<meta charset="utf-8">
<title>KJT Consulting – Window Signage</title>
<link rel="stylesheet" href="https://fonts.googleapis.com/css2?family=Open+Sans:wght@300;400;800&display=swap">
<style>
  :root {
    --stage: #8c8c8c;
    --paper: #ffffff;
    --ink: #1a1a1a;
    --accent: #e8601a;
    --band-start: #e8651a;
    --band-end: #f6b421;
    --logo-grey: #616161;
    --on-band: #ffffff;
  }
  * { margin: 0; padding: 0; box-sizing: border-box; }
  html, body {
    width: 893px;
    height: 1200px;
    overflow: hidden;
    background: var(--stage);
    font-family: "Open Sans", sans-serif;
  }
  .sign {
    position: absolute;
    left: 58px;
    background: var(--paper);
    overflow: hidden;
  }
  .sign--window-one { top: 59px;  width: 601px; height: 501px; }
  .sign--window-two { top: 607px; width: 764px; height: 535px; }

  .sign__band {
    position: absolute;
    inset: 0;
    width: 100%;
    height: 100%;
  }
  .sign__line {
    position: absolute;
    left: 0;
    right: 0;
    text-align: center;
    line-height: 1;
    white-space: nowrap;
  }
  .wordmark {
    font-weight: 400;
    color: var(--logo-grey);
    letter-spacing: 4px;
  }
  .strapline {
    font-weight: 300;
    color: var(--ink);
  }
  .strapline em {
    font-style: normal;
    color: var(--accent);
  }
  .phone {
    font-weight: 800;
    color: var(--on-band);
    letter-spacing: -0.5px;
  }
  .web {
    font-weight: 400;
    color: var(--on-band);
    letter-spacing: 0.42em;
  }

  /* window one */
  .sign--window-one .wordmark  { top: 40px;  font-size: 92px; }
  .sign--window-one .strapline { font-size: 42px; }
  .sign--window-one .strapline--first  { top: 184px; }
  .sign--window-one .strapline--second { top: 236px; }
  .sign--window-one .phone { top: 381px; font-size: 45px; }
  .sign--window-one .web   { top: 435px; font-size: 17px; }

  /* window two */
  .sign--window-two .wordmark  { top: 44px;  font-size: 100px; }
  .sign--window-two .strapline { font-size: 48px; }
  .sign--window-two .strapline--first  { top: 198px; }
  .sign--window-two .strapline--second { top: 258px; }
  .sign--window-two .phone { top: 417px; font-size: 50px; }
  .sign--window-two .web   { top: 487px; font-size: 20px; }
</style>
</head>
<body>

<section class="sign sign--window-one" aria-label="Window sign, size one">
  <svg class="sign__band" viewBox="0 0 601 501" preserveAspectRatio="none" aria-hidden="true">
    <defs>
      <linearGradient id="band-one" x1="0" y1="0" x2="1" y2="0">
        <stop offset="0" stop-color="var(--band-start)" style="stop-color: var(--band-start)"/>
        <stop offset="1" stop-color="var(--band-end)" style="stop-color: var(--band-end)"/>
      </linearGradient>
    </defs>
    <polygon points="0,389 601,293 601,501 0,501" fill="url(#band-one)"/>
  </svg>
  <div class="sign__line wordmark">KJT</div>
  <p class="sign__line strapline strapline--first">Empowering <em>businesses</em></p>
  <p class="sign__line strapline strapline--second">with <em>software</em> choice.</p>
  <p class="sign__line phone">1300 46 81 07</p>
  <p class="sign__line web">www.kjtconsulting-example.net.au</p>
</section>

<section class="sign sign--window-two" aria-label="Window sign, size two">
  <svg class="sign__band" viewBox="0 0 764 535" preserveAspectRatio="none" aria-hidden="true">
    <defs>
      <linearGradient id="band-two" x1="0" y1="0" x2="1" y2="0">
        <stop offset="0" style="stop-color: var(--band-start)"/>
        <stop offset="1" style="stop-color: var(--band-end)"/>
      </linearGradient>
    </defs>
    <polygon points="0,425 764,305 764,535 0,535" fill="url(#band-two)"/>
  </svg>
  <div class="sign__line wordmark">KJT</div>
  <p class="sign__line strapline strapline--first">Empowering <em>businesses</em></p>
  <p class="sign__line strapline strapline--second">with <em>software</em> choice.</p>
  <p class="sign__line phone">1300 46 81 07</p>
  <p class="sign__line web">www.kjtconsulting-example.net.au</p>
</section>

</body>
</html>
```